automotive repair and collision repair shop card

our company is called K.W Motor service we are a automotive repair company
we also do government inspections. the company information is on the cards. I would like you to use my new logo and create a new card and use the information from my old card. Good Luck!!

Industry/Entity Type

Car Repair

Contact Information for Business Card

Address: #417-10952 58 Ave, Surrey, BC V3X 4K8
Phone:(604) 555-0178
fax 604 555 0193
website www.kwmotorworks.example

Font styles to use
Serif
Sans Serif

Requirements
Must have
• all the information
Should not have
• the owner and there name

```html
<!DOCTYPE html>
<html lang="en">
<head>
<meta charset="utf-8">
<title>K.W Motor Service — Business Card</title>
<link rel="stylesheet" href="https://fonts.googleapis.com/css2?family=Open+Sans:wght@400;600;700&display=swap">
<style>
  :root {
    --page-bg: #e9e6e1;
    --card-white: #ffffff;
    --front-blue-dark: #1465b4;
    --front-blue-light: #2a9be2;
    --back-navy: #16173a;
    --back-slate: #3c3f78;
    --swoosh-blue: #2432b8;
    --swoosh-deep: #141a5e;
    --car-dark: #1d1f2a;
    --car-mid: #3a3e4e;
    --text-white: #ffffff;
    --text-grey: #3a3a3a;
  }
  * { margin: 0; padding: 0; box-sizing: border-box; }
  html, body {
    width: 1200px; height: 900px; overflow: hidden;
    background: var(--page-bg);
    font-family: "Open Sans", Arial, sans-serif;
  }
  .stage {
    position: relative; width: 1200px; height: 900px;
  }
  .card {
    position: absolute; left: 285px; width: 630px; height: 360px;
    background: var(--card-white); overflow: hidden;
    box-shadow: 0 8px 24px rgba(0,0,0,.25);
  }
  .card--front { top: 50px; }
  .card--back { top: 490px; }

  /* Front */
  .front-field {
    position: absolute; left: 0; right: 0; top: 22px; bottom: 38px;
    background: linear-gradient(100deg, var(--front-blue-dark) 0%, var(--front-blue-light) 100%);
  }
  .brand {
    position: absolute; display: flex; flex-direction: column; align-items: flex-end;
  }
  .brand__art {
    border-radius: 40px 60px 14px 14px;
    background: radial-gradient(ellipse at 50% 55%, var(--car-mid) 0%, var(--car-dark) 75%);
  }
  .brand__name {
    font-weight: 700; color: var(--text-white); letter-spacing: .5px;
    line-height: 1; white-space: nowrap;
  }
  .brand__tagline {
    font-weight: 400; color: var(--text-white); line-height: 1.2; white-space: nowrap;
  }
  .card--front .brand { left: 165px; top: 85px; width: 300px; }
  .card--front .brand__art { width: 270px; height: 70px; align-self: center; }
  .card--front .brand__name { font-size: 27px; margin-top: 8px; }
  .card--front .brand__tagline { font-size: 12px; }

  /* Back */
  .back-field {
    position: absolute; left: 0; right: 0; top: 24px; bottom: 50px;
    background: linear-gradient(120deg, var(--back-navy) 0%, var(--back-navy) 40%, var(--back-slate) 100%);
  }
  .back-swoosh { position: absolute; left: 0; top: 24px; width: 630px; height: 286px; }
  .card--back .brand { left: 330px; top: 42px; width: 280px; }
  .card--back .brand__art { width: 240px; height: 64px; align-self: center; }
  .card--back .brand__name { font-size: 25px; margin-top: 8px; }
  .card--back .brand__tagline { font-size: 11px; }

  .contact-list {
    position: absolute; left: 36px; top: 180px; list-style: none;
  }
  .contact-list li {
    display: flex; align-items: center; gap: 12px;
    height: 25px; color: var(--text-white); font-size: 15px;
  }
  .contact-list svg { width: 17px; height: 17px; flex: none; }
  .address {
    position: absolute; left: 44px; bottom: 16px;
    font-size: 15px; font-weight: 600; color: var(--text-grey);
  }
</style>
</head>
<body>
<main class="stage">

  <section class="card card--front" aria-label="Card front">
    <div class="front-field"></div>
    <div class="brand">
      <div class="brand__art" role="img" aria-label="Illustration of a dark sports car with silver wheels"></div>
      <div class="brand__name">K.W MOTOR SERVICE</div>
      <div class="brand__tagline">One Stop Repair Shop</div>
    </div>
  </section>

  <section class="card card--back" aria-label="Card back">
    <div class="back-field"></div>
    <svg class="back-swoosh" viewBox="0 0 630 286" preserveAspectRatio="none" aria-hidden="true">
      <defs>
        <linearGradient id="swoosh-fill" x1="0" y1="0" x2="0" y2="1">
          <stop offset="0" stop-color="var(--swoosh-blue)"/>
          <stop offset="1" stop-color="var(--swoosh-deep)"/>
        </linearGradient>
      </defs>
      <path d="M0,150 Q230,70 520,140 Q590,158 630,186 L630,286 L0,286 Z" fill="url(#swoosh-fill)"/>
      <path d="M0,286 L0,286 Q150,286 300,286 Q470,270 630,196 L630,286 Z" fill="var(--back-navy)" opacity=".55"/>
      <path d="M350,286 Q500,262 630,205 L630,286 Z" fill="var(--card-white)"/>
    </svg>

    <div class="brand">
      <div class="brand__art" role="img" aria-label="Illustration of a dark sports car with silver wheels"></div>
      <div class="brand__name">K.W MOTOR SERVICE</div>
      <div class="brand__tagline">One Stop Repair Shop</div>
    </div>

    <ul class="contact-list">
      <li>
        <svg viewBox="0 0 24 24" fill="#fff" aria-label="Fax"><rect x="6" y="2" width="12" height="6" rx="1"/><rect x="2" y="9" width="20" height="9" rx="2"/><rect x="6" y="15" width="12" height="7" rx="1" fill="#fff" stroke="#16173a" stroke-width="1.5"/></svg>
        <span>604 555 0193</span>
      </li>
      <li>
        <svg viewBox="0 0 24 24" fill="#fff" aria-label="Phone"><path d="M6.6 10.8a15 15 0 0 0 6.6 6.6l2.2-2.2a1 1 0 0 1 1-.25 11.4 11.4 0 0 0 3.6.57 1 1 0 0 1 1 1V20a1 1 0 0 1-1 1A17 17 0 0 1 3 4a1 1 0 0 1 1-1h3.5a1 1 0 0 1 1 1c0 1.25.2 2.45.57 3.6a1 1 0 0 1-.25 1z"/></svg>
        <span>(604) 555-0178</span>
      </li>
      <li>
        <svg viewBox="0 0 24 24" fill="none" stroke="#fff" stroke-width="2" aria-label="Email"><rect x="2" y="5" width="20" height="14" rx="1"/><path d="M2 6l10 7 10-7"/></svg>
        <span>info@kwmotorworks.example</span>
      </li>
      <li>
        <svg viewBox="0 0 24 24" fill="none" stroke="#fff" stroke-width="1.8" aria-label="Website"><circle cx="12" cy="12" r="10"/><ellipse cx="12" cy="12" rx="4.5" ry="10"/><path d="M2 12h20M4 7h16M4 17h16"/></svg>
        <span>www.kwmotorworks.example</span>
      </li>
    </ul>

    <p class="address">#417-10952 58 Ave, Surrey, BC V3X 4K8</p>
  </section>

</main>
</body>
</html>
```